Musician looking for catchy Web Design for promotion

My name is Bridget Colfer. I'm an Irish musician who plays the tin whistle and the flute. I'm also the leader of a traditional Irish music and dance ensemble called Rowan Road Players (www.rowanroadplayers.test) and for the past 30 years, I've toured the world performing thousands of concerts. I run an annual cruise (www.bridgetcolfercruise.test) that I would like a link to, and I'm also I'm organizing tours to Ireland that I would like a page set up for. I'm looking for a website to promote my tours and my music.

Hello Graphic Designers, I am only looking for the design of the home page to make my decision. Thank you. Bridget

Target Market(s)

Music fans of Irlsh and World Music

Industry/Entity Type

Entertainment Industry

Number of Pages Required

5+ page

Requirements
Must have
• I'm looking for a catchy design that shows a photo of me. I would like a few links....
• BIO
• TOURDATES
• BRIDGET COLFER CRUISE
• MUSICAL TOUR OF IRELAND
• CONTACT
• VIDEO
• GALLERY
• CONTACT
• MAILING LIST
• STORE
Nice to have
• we'll see!

```html
<!DOCTYPE html>
<html lang="en">
<head>
<meta charset="utf-8">
<title>Bridget Colfer — Musical Tour of Ireland</title>
<link rel="stylesheet" href="https://fonts.googleapis.com/css2?family=Lora:ital,wght@0,400;0,700;1,400&family=Allura&family=Kalam:wght@700&display=swap">
<style>
:root{
  --wood:#5a1e14;
  --wood-dark:#3b120c;
  --topbar:#4a1a12;
  --cream:#f4f1ea;
  --paper:#f1eee6;
  --ink:#5b1d12;
  --text:#5a514a;
  --gold:#cdbb7a;
  --gold-dark:#a8964f;
  --btn:#3f3d3b;
  --footer:#24100b;
  --footer-bar:#3a1009;
  --hero-a:#f0c98a;
  --hero-b:#c87a3a;
}
*{margin:0;padding:0;box-sizing:border-box}
html,body{width:1200px;height:2983px;overflow:hidden}
body{position:relative;background:linear-gradient(90deg,#4a170f,#6a2418 30%,#5a1e14 50%,#6a2418 70%,#4a170f);font-family:"Lora",serif;color:var(--text)}
.abs{position:absolute}
.topbar{left:0;top:0;width:1200px;height:31px;background:var(--topbar);font:11px Arial,sans-serif;color:#e8d9c8}
.topbar .contact{left:190px;top:9px}
.topbar .connect{left:876px;top:9px}
.dot{position:absolute;width:22px;height:22px;border-radius:50%;background:#f1e6d6;top:4px}
.header-ribbon{left:131px;top:50px;width:938px;height:95px;background:#e6e2d8;clip-path:polygon(0 0,100% 0,97% 50%,100% 100%,0 100%,3% 50%)}
.header{left:154px;top:31px;width:892px;height:94px;background:var(--cream);border-bottom:1px solid #d8d2c4}
.brand{left:190px;top:62px;display:flex;align-items:center;gap:10px;color:#1f1a16;font-size:14px}
.brand .mark{width:22px;height:22px;border-radius:50%;background:#2b2420}
.brand small{display:block;font-size:9px}
.nav{left:468px;top:73px;display:flex;gap:22px;font-size:12px;color:var(--ink)}
.hero{left:171px;top:133px;width:858px;height:419px;background:radial-gradient(circle at 60% 30%,#fbe7bf,var(--hero-a) 40%,var(--hero-b))}
.hero-photo{left:190px;top:160px;width:300px;height:392px;background:linear-gradient(#6b5a4a,#3a3e3a);border-radius:40px 40px 0 0}
.hero-inst{left:560px;top:300px;width:469px;height:252px;background:linear-gradient(90deg,#b5602a,#d08040,#a2451d)}
.hero h1{left:497px;top:170px;font-size:54px;font-weight:400;color:var(--ink);letter-spacing:1px}
.hero-sub{left:497px;top:234px;font-size:16.5px;line-height:21px;color:#3f2a20}
.cruise{left:171px;top:552px;width:858px;height:134px;background:var(--cream);border-bottom:4px solid #e8cfa0}
.cruise h2{left:191px;top:576px;font-size:35px;font-weight:400;color:var(--ink)}
.cruise-meta{left:194px;top:624px;font-size:17px;color:#4a3a30;display:flex;align-items:center;gap:6px}
.badge{left:866px;top:560px;width:114px;height:114px;border-radius:50%;border:1px solid #cdbfa8;background:#f7f4ee;font:700 19px/22px "Kalam",cursive;color:#3a1a10;text-align:center;padding-top:22px;transform:rotate(-18deg)}
.panel{left:163px;top:686px;width:874px;height:1662px;background:var(--paper)}
.script{left:0;width:1200px;top:712px;text-align:center;font:62px "Allura",cursive;color:var(--ink)}
.rule{left:275px;top:784px;width:652px;border-top:1px dashed #8a6b5a}
.portrait{left:507px;top:814px;width:186px;height:186px;border-radius:50%;background:radial-gradient(#b87a3a,#4a2b18);border:3px dotted #6a1e12}
.bio{left:205px;top:1022px;width:790px;text-align:center;font-size:13.5px;line-height:20.5px}
.bio p{margin-bottom:12px}
.btn{display:block;background:var(--btn);color:#f3eee6;font-size:13.5px;text-align:center;line-height:42px;box-shadow:0 0 0 1px #777 inset}
.ribbon-tail{width:170px;height:60px;background:var(--gold-dark)}
.ribbon-tail.l{clip-path:polygon(0 55%,100% 0,100% 100%,20% 100%)}
.ribbon-tail.r{clip-path:polygon(0 0,100% 55%,80% 100%,0 100%)}
.ribbon{left:163px;width:876px;background:linear-gradient(#d9c98e,var(--gold));color:#2b1a10;border-bottom:3px solid #b9a66a}
.info-band{top:1315px;height:55px;display:flex;justify-content:space-between;align-items:center;padding:0 44px;font-size:17.5px}
.sec-title{font-size:20px;color:var(--ink);display:flex;align-items:center;gap:6px}
.sec-title i{display:block;border-top:1px dashed #8a6b5a}
.video{left:191px;top:1479px;width:397px;height:223px;background:linear-gradient(120deg,#1a1640,#3a2a50 50%,#a0705a)}
.vbar{position:absolute;left:0;bottom:0;width:100%;height:22px;background:#111;color:#aaa;font:8px Arial,sans-serif;display:flex;align-items:center;gap:8px;padding:0 8px}
.vbar .track{flex:1;height:2px;background:#666}
.thumb{width:87px;height:101px}
.quotes{left:230px;top:1928px;width:740px;text-align:center;font-size:14px;line-height:20.5px}
.quotes blockquote{font-style:italic;margin-bottom:2px}
.quotes cite{display:block;font-style:normal;color:#2a1a14;margin-bottom:20px}
.footer{left:0;top:2348px;width:1200px;height:588px;background:radial-gradient(ellipse at 60% 50%,#3a1a10,var(--footer))}
.f-h{font-size:29px;color:#f3ece2;font-weight:400}
.f-text{color:#e9dfd2;font-size:12.5px;line-height:21px}
.field{position:absolute;border:1px solid #8a7f78;background:#0e0705;color:#8a807a;font-size:12px;padding:9px 11px}
.submit{left:540px;top:2788px;width:249px;height:43px;border:1px solid #8a7f78;color:#f3ece2;font-size:18px;text-align:center;line-height:41px}
.soc{width:36px;height:36px;border-radius:50%;background:#9a9590}
.bottombar{left:0;top:2936px;width:1200px;height:47px;background:var(--footer-bar);color:#d8cabb;font-size:10.5px}
</style>
</head>
<body>
<div class="abs topbar">
  <span class="abs contact">Phone: 000 000 0000 &nbsp;&nbsp; E-mail: book@bridgetcolfercruise.test</span>
  <span class="abs connect">Connect with us</span>
  <span class="dot" style="left:958px"></span><span class="dot" style="left:988px"></span>
</div>

<div class="abs header-ribbon"></div>
<header class="abs header"></header>
<div class="abs brand"><span class="mark"></span><div>BRIDGET COLFER'S<small>MUSICAL TOUR OF IRELAND</small></div></div>
<nav class="abs nav"><span>Home</span><span>About</span><span>Bridget Colfer Cruise</span><span>Ireland Tour</span><span>Video</span><span>Gallery</span><span>Store</span><span>Contact</span></nav>

<section class="abs hero"></section>
<div class="abs hero-inst" role="img" aria-label="Row of flutes and tin whistles in a cloth case"></div>
<div class="abs hero-photo" role="img" aria-label="Bridget Colfer smiling and holding a tin whistle"></div>
<h1 class="abs hero" style="background:none;width:auto;height:auto;left:497px;top:170px">BRIDGET COLFER</h1>
<p class="abs hero-sub">is considered one of the greatest musicians and personalities<br>in the history of Irish music in America.</p>

<section class="abs cruise"></section>
<h2 class="abs cruise">Bridget Colfer's Folk'n Irish Cruise</h2>
<div class="abs cruise-meta">
  <svg width="15" height="16" viewBox="0 0 15 16"><path d="M7.5 1a5 5 0 0 1 5 5c0 4-5 9-5 9s-5-5-5-9a5 5 0 0 1 5-5z" fill="none" stroke="#4a3a30" stroke-width="1.5"/><circle cx="7.5" cy="6" r="1.8" fill="none" stroke="#4a3a30"/></svg>
  Seafarer Gem, &nbsp;&nbsp;
  <svg width="18" height="16" viewBox="0 0 18 16"><rect x="1" y="2" width="13" height="12" fill="none" stroke="#4a3a30" stroke-width="1.5"/><line x1="1" y1="6" x2="14" y2="6" stroke="#4a3a30" stroke-width="1.5"/><circle cx="14" cy="12" r="3.5" fill="#f4f1ea" stroke="#4a3a30"/></svg>
  Sunday, 05/29/2016 from New York
</div>
<div class="abs badge">New<br>Booking<br>For 2017</div>

<main class="abs panel"></main>
<div class="abs script">Bridget Colfer</div>
<div class="abs rule"></div>
<div class="abs portrait" role="img" aria-label="Portrait of Bridget Colfer"></div>
<div class="abs bio">
  <p>BRIDGET COLFER is considered one of the greatest musicians and personalities in the history of Irish music in America. She was born in the Bronx, New York of Irish parents, and she is the second oldest of seven children raised in a musical household. Her mother Maura hails from Miltown Malbay, County Clare and her father Tom, an All-Ireland Champion accordion player, was a native of Portumna, County Galway.</p>
  <p>Bridget was exposed to the finest Irish traditional music early in her life, listening to her father and his friends play music at family gatherings and social events. She began taking lessons from legendary flutist Liam Doran, and within a few short years she won the All-Ireland Championship on both the concert flute and tin whistle. In 1984, Bridget became the first American to win the coveted Senior All-Ireland Championship on the whistle.</p>
</div>
<a class="abs btn" style="left:535px;top:1225px;width:130px">READ MORE</a>

<div class="abs ribbon-tail l" style="left:98px;top:1330px"></div>
<div class="abs ribbon-tail r" style="left:930px;top:1330px"></div>
<div class="abs ribbon info-band"><span>All other countries call: 00-1-555-014-2270 extension 4410</span><span>Email: book@bridgetcolfercruise.test</span></div>

<div class="abs sec-title" style="left:190px;top:1439px">See Bridget Colfer Videos <i style="width:156px"></i></div>
<div class="abs sec-title" style="left:612px;top:1439px">Photo Gallery <i style="width:152px"></i></div>
<div class="abs video" role="img" aria-label="Concert video of Bridget Colfer on stage">
  <div class="vbar"><span>❚❚</span><span>00:10</span><span class="track"></span><span>04:07</span></div>
</div>
<div class="abs thumb" style="left:613px;top:1479px;background:#8a6a50" role="img" aria-label="Hands on a flute"></div>
<div class="abs thumb" style="left:716px;top:1479px;background:#6a4a34" role="img" aria-label="Portrait photo"></div>
<div class="abs thumb" style="left:820px;top:1479px;background:#5a5040" role="img" aria-label="Photo outdoors with whistle"></div>
<div class="abs thumb" style="left:923px;top:1479px;background:#6a8078" role="img" aria-label="Performer with whistle"></div>
<div class="abs thumb" style="left:613px;top:1600px;background:#5a6a88" role="img" aria-label="Concert hall building"></div>
<div class="abs thumb" style="left:716px;top:1600px;background:#5a2a30" role="img" aria-label="Ensemble on stage"></div>
<div class="abs thumb" style="left:820px;top:1600px;background:#3a2a2a" role="img" aria-label="Group of musicians"></div>
<div class="abs thumb" style="left:923px;top:1600px;background:#5a1a14" role="img" aria-label="Flute player in red on stage"></div>
<a class="abs btn" style="left:308px;top:1727px;width:163px">VIEW MORE VIDEO</a>
<a class="abs btn" style="left:730px;top:1727px;width:163px">VIEW MORE PHOTO</a>

<div class="abs ribbon-tail l" style="left:98px;top:1842px"></div>
<div class="abs ribbon-tail r" style="left:930px;top:1842px"></div>
<div class="abs ribbon" style="top:1827px;height:55px;text-align:center;line-height:55px;font-size:24px">WHAT THE CRITICS ARE SAYING ABOUT BRIDGET COLFER....</div>

<div class="abs quotes">
  <blockquote>“When distinguished tin whistle or flute players over the past quarter of a century come to mind, Irish traditional music aficionados invariably will add Bridget Colfer's name to the list. Her music is pure art, compelling and creative, vibrant and virtuosic. It is filled with style, substance, sensitivity and soul.”</blockquote>
  <cite>Owen Hartley, The Celtic Courier</cite>
  <blockquote>“Colfer has become a preeminent Irish flute and whistle virtuoso, constantly in demand for session and commercial work. She has gone on to become both a dazzling technician and spellbindingly articulate interpreter of slow airs. She displays a range of texture and emotion that many singers would envy.”</blockquote>
  <cite>Dana Whitcombe, The Harbor Ledger</cite>
  <blockquote>“Bridget Colfer is one of New York's finest flute and whistle players, not to mention the only American born, All-Ireland Champion on the whistle. Her music sizzles with life, outstanding for it's total command of technique and remarkable breath control. Her whistle playing flows smoothly, showcasing a dazzling sequence of devices, cuts, crans and rolls known only to the brave and to the good.”</blockquote>
  <cite>Siobhan Kerrigan, The Western Herald (Galway)</cite>
</div>
<a class="abs btn" style="left:535px;top:2270px;width:130px">VIEW MORE</a>

<footer class="abs footer" role="img" aria-label="Faint photo of a theatre marquee behind the footer"></footer>
<h3 class="abs f-h" style="left:171px;top:2426px">CONTACT</h3>
<div class="abs" style="left:171px;top:2480px;color:#f3ece2;font-size:21px">Bridget Colfer</div>
<div class="abs f-text" style="left:171px;top:2514px">Lorem ipsum dolor<br>sit amet, consectetur<br>adipiscing elit</div>
<div class="abs f-text" style="left:171px;top:2587px">✉ book@bridgetcolfercruise.test</div>
<div class="abs f-text" style="left:171px;top:2619px">✆ Tel: 555-019-4836</div>
<h3 class="abs f-h" style="left:171px;top:2654px">GET IN TOUCH</h3>
<div class="abs soc" style="left:171px;top:2707px"></div>
<div class="abs soc" style="left:222px;top:2707px"></div>
<h3 class="abs f-h" style="left:540px;top:2426px">SIGN UP FOR BRIDGET COLFER'S</h3>
<div class="field" style="left:540px;top:2492px;width:488px;height:34px">Name</div>
<div class="field" style="left:540px;top:2540px;width:488px;height:34px">Email</div>
<div class="field" style="left:540px;top:2589px;width:238px;height:34px">Zip</div>
<div class="field" style="left:790px;top:2589px;width:238px;height:34px">Birth Year</div>
<div class="field" style="left:540px;top:2638px;width:488px;height:129px">Message</div>
<div class="abs submit">Add me to the mailing list</div>

<div class="abs bottombar">
  <span class="abs" style="left:171px;top:17px">Home &nbsp;/&nbsp; About &nbsp;/&nbsp; Bridget Colfer Cruise &nbsp;/&nbsp; Ireland Tour &nbsp;/&nbsp; Video &nbsp;/&nbsp; Gallery &nbsp;/&nbsp; Store &nbsp;/&nbsp; Contact</span>
  <span class="abs" style="right:171px;top:17px">© 2016 rowanroadplayers.test. All rights reserved.</span>
</div>
</body>
</html>
```